Gala Event Program - Italian

Need a program with the exact same layout/structure as attached. The new theme for the event this year will be: Notte di Lanterne Dorate, Under Golden Lantern Light. The look that we are going for is Italian garden party. The page sizes should also be the same as previously - 8.5 X 11.

The image sizes relative to pring should remain roughly the same for the individual and group pages.

```html
<!DOCTYPE html>
<html lang="en">
<head>
<meta charset="utf-8">
<title>Notte di Lanterne Dorate – Gala Program</title>
<link rel="stylesheet" href="https://fonts.googleapis.com/css2?family=Montserrat:wght@400;500;600;700&family=Pinyon+Script&family=Allura&display=swap">
<style>
:root{
  --bg-left:#f1c8b8;
  --bg-right:#d58e7d;
  --frame:#ffffff;
  --blush:#fbf1ee;
  --rose:#e2a893;
  --rose-line:#d9a08f;
  --ink:#2b2020;
  --body:#4a3a38;
  --cover:#111010;
  --copper:#c98a72;
  --petal:rgba(214,128,155,.78);
  --leaf:rgba(150,172,138,.55);
}
*{margin:0;padding:0;box-sizing:border-box}
html,body{width:1200px;height:786px;overflow:hidden}
body{
  position:relative;
  background:linear-gradient(90deg,var(--bg-left),var(--bg-right));
  font-family:"Montserrat",sans-serif;
  color:var(--ink);
}
.page{
  position:absolute;width:275px;height:353px;
  background:var(--frame);border-radius:5px;
  box-shadow:0 1px 3px rgba(120,60,50,.18);
}
.sheet{position:absolute;inset:5px;background:var(--blush);border-radius:1px;overflow:hidden}
.sheet.dark{background:linear-gradient(160deg,#171616,var(--cover) 60%,#0b0b0b)}
.deco{position:absolute;inset:0;width:275px;height:353px}
.abs{position:absolute}
.center{left:0;right:0;text-align:center}

.floral{position:absolute;pointer-events:none}
.floral-tl{left:5px;top:5px;width:40px;height:48px;
  background:radial-gradient(ellipse at 20% 20%,var(--leaf),rgba(214,170,180,.35) 45%,transparent 72%)}
.floral-tr{right:5px;top:5px;width:72px;height:88px;
  background:radial-gradient(ellipse at 75% 30%,var(--petal),rgba(196,110,140,.45) 38%,var(--leaf) 52%,transparent 74%)}
.floral-bl{left:5px;bottom:5px;width:74px;height:92px;
  background:radial-gradient(ellipse at 30% 70%,var(--petal),rgba(196,110,140,.45) 38%,var(--leaf) 54%,transparent 74%)}
.floral-br{right:5px;bottom:5px;width:36px;height:42px;
  background:radial-gradient(ellipse at 80% 80%,rgba(130,90,120,.55),var(--leaf) 40%,transparent 72%)}

.eyebrow{font-weight:600;color:var(--rose);letter-spacing:.3px;line-height:1}
.script{font-family:"Pinyon Script",cursive;color:var(--ink);line-height:1;font-weight:400}

/* cover */
.cover-title{font-family:"Allura",cursive;color:var(--copper);font-size:12.5px;line-height:1}
.cover-sub{font-size:3.6px;letter-spacing:.9px;color:var(--copper);text-transform:uppercase}

/* schedule */
.time{font-weight:700;font-size:8px;line-height:1}
.time.big{font-size:9px}
.item{font-size:4.5px;line-height:1;color:var(--body)}

/* sponsor */
.sponsor-name{font-weight:700;font-size:7px;color:var(--ink);letter-spacing:.3px;line-height:1.2;text-align:center}

/* committee */
.committee{list-style:none;text-align:center}
.committee li{font-size:5px;line-height:10.9px;color:var(--ink);text-transform:uppercase}

/* seniors */
.bio{font-size:4.5px;line-height:8.3px;color:var(--body);text-align:left}
.caption{font-size:4.6px;line-height:8.3px;color:var(--body);text-align:center}
</style>
</head>
<body>

<!-- Cover -->
<section class="page" style="left:24px;top:31px">
  <div class="sheet dark" role="img" aria-label="Dark palm-leaf pattern background"></div>
  <svg class="deco" viewBox="0 0 275 353" aria-hidden="true">
    <g fill="none" stroke="var(--copper)" stroke-width=".8">
      <polygon points="72,176 104,120 172,120 204,176 172,232 104,232"/>
      <polygon points="92,144 132,100 192,128 190,204 148,252 88,222"/>
    </g>
  </svg>
  <div class="abs center cover-title" style="top:166px">Notte di Lanterne Dorate</div>
  <div class="abs center cover-sub" style="top:184px">Under Golden Lantern Light</div>
</section>

<!-- Evening schedule -->
<section class="page" style="left:316px;top:31px">
  <div class="sheet"></div>
  <div class="floral floral-tl" role="img" aria-label="Watercolour greenery sprig"></div>
  <div class="floral floral-tr" role="img" aria-label="Watercolour pink peonies and leaves"></div>
  <div class="floral floral-bl" role="img" aria-label="Watercolour pink roses and leaves"></div>
  <div class="floral floral-br" role="img" aria-label="Watercolour berry sprig"></div>
  <svg class="deco" viewBox="0 0 275 353" aria-hidden="true">
    <polygon points="50,70 88,25 175,25 192,68 158,118 75,118" fill="#fff"/>
    <polygon points="62,60 100,18 176,30 186,82 150,124 72,112" fill="none" stroke="var(--rose-line)" stroke-width=".5"/>
  </svg>
  <div class="abs eyebrow" style="left:101px;top:53px;font-size:12px">EVENING</div>
  <div class="abs script" style="left:136px;top:67px;font-size:17px">Festivities</div>

  <div class="abs center time" style="top:133px">7:30 PM</div>
  <div class="abs center item" style="top:147px">Cocktail Reception (Cash Bar) Heads and Tails Sales Open</div>
  <div class="abs center item" style="top:157px">Gold Grab Cupcake Sales Open</div>
  <div class="abs center time" style="top:173px">8:00 PM</div>
  <div class="abs center item" style="top:187px">Presentation of Belles and Beaux</div>
  <div class="abs center time" style="top:202px">9:15 PM</div>
  <div class="abs center item" style="top:216px">Heads and Tails</div>
  <div class="abs center item" style="top:225px">Dinner Immediately Following</div>
  <div class="abs center item" style="top:235px">Heads and Tails</div>
  <div class="abs center time" style="top:249px">9:45 PM</div>
  <div class="abs center item" style="top:262px">Presentation of Belles and Beaux</div>
  <div class="abs center time" style="top:277px">11:45 PM</div>
  <div class="abs center item" style="top:290px">Drawing for $1000 Gift Card</div>
  <div class="abs center time big" style="top:301px">12:00 Midnight</div>
  <div class="abs center item" style="top:316px">Conclusion</div>
</section>

<!-- Program sponsor -->
<section class="page" style="left:611px;top:31px">
  <div class="sheet"></div>
  <div class="floral floral-tl" role="img" aria-label="Watercolour greenery sprig"></div>
  <div class="floral floral-tr" role="img" aria-label="Watercolour pink peonies and leaves"></div>
  <div class="floral floral-bl" role="img" aria-label="Watercolour pink roses and leaves"></div>
  <div class="floral floral-br" role="img" aria-label="Watercolour berry sprig"></div>
  <svg class="deco" viewBox="0 0 275 353" aria-hidden="true">
    <polygon points="52,122 95,42 200,36 220,118 178,190 80,190" fill="#fff"/>
    <polygon points="68,100 122,28 202,56 216,142 150,198 70,172" fill="none" stroke="var(--rose-line)" stroke-width=".5"/>
  </svg>
  <div class="abs eyebrow" style="left:67px;top:80px;font-size:18px;font-weight:700">PROGRAM</div>
  <div class="abs script" style="left:124px;top:106px;font-size:27px">Sponsor</div>
  <div class="abs sponsor-name" style="left:170px;top:186px;width:66px">HARBORLINE<br>EVENTS</div>
  <div class="abs script" style="left:30px;top:218px;font-size:13px">Special thanks</div>
  <div class="abs script" style="left:70px;top:246px;font-size:28px">Marco Bellini</div>
  <div class="abs script" style="left:145px;top:284px;font-size:12px">for program design</div>
</section>

<!-- Committee -->
<section class="page" style="left:901px;top:31px">
  <div class="sheet"></div>
  <div class="floral floral-tl" role="img" aria-label="Watercolour greenery sprig"></div>
  <div class="floral floral-tr" role="img" aria-label="Watercolour pink peonies and leaves"></div>
  <div class="floral floral-bl" role="img" aria-label="Watercolour pink roses and leaves"></div>
  <div class="floral floral-br" role="img" aria-label="Watercolour berry sprig"></div>
  <svg class="deco" viewBox="0 0 275 353" aria-hidden="true">
    <polygon points="72,88 100,38 180,36 198,88 170,138 98,140" fill="#fff"/>
    <polygon points="85,70 125,30 190,62 186,122 140,150 90,126" fill="none" stroke="var(--rose-line)" stroke-width=".5"/>
  </svg>
  <div class="abs eyebrow" style="left:86px;top:67px;font-size:14.5px;font-weight:700">SYMPHONY</div>
  <div class="abs eyebrow" style="left:86px;top:83px;font-size:14.5px;font-weight:700">BAL</div>
  <div class="abs script" style="left:124px;top:88px;font-size:18px">Committee</div>
  <ul class="abs center committee" style="top:166px">
    <li>Rosalind Avery - Chair</li>
    <li>Dana Whitmore - President, Ex-Officio</li>
    <li>Priya Nolan</li>
    <li>Margot Ellison</li>
    <li>Celeste Hwang</li>
    <li>Tessa Brandt</li>
    <li>Naomi Kerr</li>
    <li>Lydia Fontaine</li>
    <li>Renata Osborne</li>
    <li>Joanna Pike</li>
    <li>Ines Calloway</li>
    <li>Harriet Quinlan</li>
    <li>Vivian Oakes</li>
    <li>Beatrix Lund</li>
    <li>Maribel Ortega</li>
  </ul>
</section>

<!-- Seniors: individual -->
<section class="page" style="left:169px;top:402px">
  <div class="sheet"></div>
  <div class="floral floral-tl" role="img" aria-label="Watercolour greenery sprig"></div>
  <div class="floral floral-tr" role="img" aria-label="Watercolour pink peonies and leaves"></div>
  <div class="floral floral-bl" role="img" aria-label="Watercolour pink roses and leaves"></div>
  <div class="floral floral-br" role="img" aria-label="Watercolour berry sprig"></div>
  <svg class="deco" viewBox="0 0 275 353">
    <defs>
      <linearGradient id="portraitOne" x1="0" y1="0" x2="0" y2="1">
        <stop offset="0" stop-color="#b79773"/>
        <stop offset=".5" stop-color="#d8b48a"/>
        <stop offset="1" stop-color="#9a2a33"/>
      </linearGradient>
      <linearGradient id="portraitTwo" x1="0" y1="0" x2="0" y2="1">
        <stop offset="0" stop-color="#cdb89a"/>
        <stop offset=".55" stop-color="#8a6a55"/>
        <stop offset="1" stop-color="#1c1718"/>
      </linearGradient>
    </defs>
    <polygon points="6,118 36,62 104,60 136,118 104,178 36,180" fill="none" stroke="var(--rose-line)" stroke-width=".5"/>
    <polygon role="img" aria-label="Senior portrait of Chiara Elise Belmonte in a red gown" points="13,124 42,70 102,68 131,124 102,180 42,182" fill="url(#portraitOne)"/>
    <polygon points="144,266 176,206 238,206 268,266 236,328 174,328" fill="none" stroke="var(--rose-line)" stroke-width=".5"/>
    <polygon role="img" aria-label="Senior portrait of Noemi Vale Castillo in a black gown" points="149,268 178,213 234,211 263,268 234,322 178,324" fill="url(#portraitTwo)"/>
  </svg>
  <div class="abs center eyebrow" style="top:17px;font-size:11.5px">SENIORS</div>
  <div class="abs eyebrow" style="left:137px;top:52px;font-size:11px">CHIARA ELISE</div>
  <div class="abs script" style="left:178px;top:64px;font-size:15px">Belmonte</div>
  <p class="abs bio" style="left:137px;top:85px;width:124px">Chiara Elise Belmonte, 18, is the daughter of Mr. &amp; Mrs. Vincent Belmonte. She is the granddaughter of Mr. Roland Pierce &amp; Mrs. Adele Belmonte and Mr. Thomas Brenner and Mrs. Louise Marie Brenner. Chiara attends Northgate Academy Charter School. She is an active member of the Grace Community Church youth choir. Chiara is a Silver Ball Foundation Princess and has been a four-year member of the Riverbend Symphony Guild. She is a State Scholar student and has earned the Honor Roll at Northgate. Chiara plans to attend Westbrook University and major in Interior Design.</p>
  <div class="abs eyebrow" style="left:19px;top:195px;font-size:11px">NOEMI</div>
  <div class="abs script" style="left:50px;top:207px;font-size:15px">Vale Castillo</div>
  <p class="abs bio" style="left:18px;top:230px;width:127px">Noemi Vale Castillo, 18, is the daughter of Mr. &amp; Mrs. Adrian Castillo. She is the granddaughter of Mr. &amp; Mrs. Hector Castillo, Ms. Marguerite Lowell, and the late Mr. Samuel Lowell. Noemi attends Lakeview High School where she is in the top 5% of her class. She is a member of State Scholars, National Honor Society, Key Club, and the Student Leadership Council. She is a four-year member of the Varsity Falcon Steps Dance Team and serves as current Captain. She is also an eight-year member of Center Stage Dance Team with Donna Reyes's Dance Studio.</p>
</section>

<!-- Seniors: group -->
<section class="page" style="left:462px;top:402px">
  <div class="sheet"></div>
  <div class="floral floral-tl" role="img" aria-label="Watercolour greenery sprig"></div>
  <div class="floral floral-tr" role="img" aria-label="Watercolour pink peonies and leaves"></div>
  <div class="floral floral-bl" role="img" aria-label="Watercolour pink roses and leaves"></div>
  <div class="floral floral-br" role="img" aria-label="Watercolour berry sprig"></div>
  <svg class="deco" viewBox="0 0 275 353">
    <defs>
      <linearGradient id="groupPhoto" x1="0" y1="0" x2="0" y2="1">
        <stop offset="0" stop-color="#d9cfc0"/>
        <stop offset=".25" stop-color="#a9634a"/>
        <stop offset=".65" stop-color="#8e5a4c"/>
        <stop offset="1" stop-color="#8f877a"/>
      </linearGradient>
    </defs>
    <polyline points="20,288 20,133 254,133 254,140" fill="none" stroke="var(--rose-line)" stroke-width=".8"/>
    <polyline points="254,222 254,288 20,288" fill="none" stroke="var(--rose-line)" stroke-width=".8"/>
    <rect role="img" aria-label="Group photo of the senior class posed in gowns and suits in front of a brick house" x="25" y="137" width="225" height="145" fill="url(#groupPhoto)"/>
  </svg>
  <div class="abs center eyebrow" style="top:36px;font-size:11.5px">SENIORS</div>
  <p class="abs caption" style="left:34px;top:54px;width:207px">Back Row: Chiara Belmonte, Noemi Castillo, Priscilla Hartman, Wren Abernathy, Julian Okafor, Dominic Lyle, Rafael Quint, Esme Thornbury, Celia Marsh, Ivy Kendrick, and Paloma Reinholt<br>Front Row: Tobias Grange, Fern Hollis, Margo Pell, and Sabine Duarte *Not Pictured: Felix Amsel</p>
</section>

<!-- Back cover -->
<section class="page" style="left:755px;top:402px">
  <div class="sheet dark" role="img" aria-label="Dark palm-leaf pattern background"></div>
</section>

</body>
</html>
```